QORVIX needs a new business card!

QORVIX is a group of gaming enthusiasts who are looking for a new corporate business card.

The typeface should be modern and minimalist with attention paid to spacing between the letters and the letters 'qorvix' look relative to each other.

Should clean, crisp and minimalist - looking serious overall but with slight tweaks to the letters to make them look playful...

Black on white is fine.

Details on the card should include:
-the word 'qorvix'
-a job title (use any, for e.g. founder)
-a name (e.g. Ned Pallister)
-phone number
-email address

For inspiration: http://brevant.tamblework-cdn.example/wp-content/uploads/2013/07/kelo-1.jpg

Target Market(s)

Video gaming enthusiasts

Industry/Entity Type

Business

Requirements
Must have
• Black letter on white background.
The word "qorvix"
Nice to have
• Maybe use a conservative font like Gibraltar or Helvetica and tweaking each letter individually.

You can insert normal job titles under the "qorvix" typeface
Should not have
• Should not be cartoony or childish fonts. No colors.

```html
<!DOCTYPE html>
<html lang="en">
<head>
<meta charset="utf-8">
<title>QORVIX business card</title>
<link rel="stylesheet" href="https://fonts.googleapis.com/css2?family=Varela+Round&display=swap">
<style>
  :root {
    --stage: #e9e7e4;
    --card-front: #ffffff;
    --card-front-shade: #ececec;
    --card-back-top: #4a4a4a;
    --card-back-bottom: #141414;
    --ink: #2b2b2b;
    --ink-soft: #555555;
    --icon: #474747;
    --paper: #ffffff;
  }
  * { margin: 0; padding: 0; box-sizing: border-box; }
  html, body {
    width: 1200px;
    height: 1200px;
    overflow: hidden;
    background: var(--stage);
    font-family: "Varela Round", "Helvetica Neue", Arial, sans-serif;
  }
  .canvas {
    position: relative;
    width: 1200px;
    height: 1200px;
  }
  .card {
    position: absolute;
    left: 240px;
    width: 720px;
    height: 412px;
    border-radius: 2px;
    box-shadow: 0 10px 28px rgba(0, 0, 0, 0.18);
    overflow: hidden;
  }
  .card--front {
    top: 130px;
    background: radial-gradient(ellipse at 55% 45%, var(--card-front) 45%, var(--card-front-shade) 100%);
  }
  .card--back {
    top: 628px;
    background: radial-gradient(ellipse at 45% 20%, var(--card-back-top) 0%, var(--card-back-bottom) 80%);
  }
  .wordmark {
    position: absolute;
    left: 0;
    right: 0;
    text-align: center;
    font-size: 70px;
    letter-spacing: 4px;
    line-height: 1;
  }
  .card--front .wordmark { top: 92px; color: var(--ink); }
  .card--back .wordmark { top: 168px; color: var(--paper); }

  .contact-list {
    position: absolute;
    left: 442px;
    top: 218px;
    list-style: none;
  }
  .contact-list li {
    display: flex;
    align-items: center;
    height: 34px;
    font-size: 19px;
    color: var(--ink);
  }
  .contact-icon {
    width: 25px;
    height: 25px;
    border-radius: 50%;
    background: var(--icon);
    color: var(--paper);
    font-size: 15px;
    line-height: 25px;
    text-align: center;
    margin-right: 10px;
    flex: none;
  }
  .holder {
    position: absolute;
    left: 118px;
    top: 292px;
    color: var(--ink-soft);
  }
  .holder-name {
    font-size: 44px;
    line-height: 1;
    font-weight: 400;
  }
  .holder-title {
    font-size: 23px;
    margin-left: 68px;
    margin-top: 2px;
  }
</style>
</head>
<body>
<main class="canvas">
  <section class="card card--front" aria-label="Card front">
    <div class="wordmark">QORVIX</div>
    <ul class="contact-list">
      <li><span class="contact-icon">p</span>999 9999 999</li>
      <li><span class="contact-icon">e</span>nedpallister@qorvix.com</li>
      <li><span class="contact-icon">w</span>www.qorvix.com</li>
    </ul>
    <div class="holder">
      <h1 class="holder-name">Ned Pallister</h1>
      <p class="holder-title">founder</p>
    </div>
  </section>
  <section class="card card--back" aria-label="Card back">
    <div class="wordmark">QORVIX</div>
  </section>
</main>
</body>
</html>
```